New corporate stationery design for UK train leasing company

In advance of an office move later this year we are looking to redesign all our corporate stationery (business cards, letterhead, compliment slips, envelopes etc) as well as small branded items (such as mouse mats, drink mats, etc).

We wish to keep the same logo and corporate colours but are looking for a modern, fresh look that will tie in our stationery more with the look of our website and our PowerPoint template. We have a strapline, "Track Crews, True Knowhow" that we would like to incorporate into the stationery design and also need to include a "TEMLO" logo on the bottom of the letterhead/compliment slips. We have two offices so will need letterhead and compliment slips with both addresses.

The files attached include different versions of our logo (the main one is the black with green halo, file 1 or 3), our brand guidelines summary (including Pantone colours), the TEMLO logo and PowerPoint template.

More information about the business can be found at www.fernholtrail.co.uk.

If you have any questions please let me know.

I look forward to seeing the designs!
Regards
Moira

Target Market(s)

Main audience are train operators, rail industry suppliers, passenger transport groups, government and other political organisations, financiers/lenders.

Industry/Entity Type

Business

```html
<!DOCTYPE html>
<html lang="en">
<head>
<meta charset="utf-8">
<title>Fernhol Rail – Corporate Stationery</title>
<link rel="stylesheet" href="https://fonts.googleapis.com/css2?family=Arimo:wght@400;700&family=Barlow:wght@600&display=swap">
<style>
  :root {
    --brand-green: #1aa38a;
    --ink: #1d1d1d;
    --navy: #2a2a5c;
    --paper: #ffffff;
    --backdrop: #e9e6e1;
    --label: #222222;
    --photo-light: #8e9ba6;
    --photo-dark: #5a5c56;
  }
  * { box-sizing: border-box; margin: 0; padding: 0; }
  html, body { width: 1200px; height: 946px; overflow: hidden; }
  body {
    position: relative;
    background: var(--backdrop);
    font-family: "Arimo", Arial, sans-serif;
    color: var(--ink);
  }
  .item-label {
    position: absolute;
    font-family: "Barlow", "Arial Narrow", sans-serif;
    font-weight: 600;
    font-size: 15px;
    color: var(--label);
    white-space: nowrap;
  }
  .sheet { position: absolute; background: var(--paper); }

  .wordmark {
    font-family: "Arimo", Arial, sans-serif;
    font-weight: 400;
    color: var(--ink);
    white-space: nowrap;
    line-height: 1;
  }
  .strapline {
    color: var(--brand-green);
    font-size: 5px;
    line-height: 1.35;
    margin-top: 5px;
  }
  .address {
    border-left: 1px solid var(--brand-green);
    padding-left: 5px;
    font-size: 5.5px;
    line-height: 1.3;
    color: var(--ink);
  }
  .address .company { color: var(--brand-green); font-weight: 700; }
  .partner-name {
    font-family: "Arimo", Arial, sans-serif;
    font-weight: 700;
    color: var(--navy);
    line-height: 1;
  }

  /* Letterhead */
  .letterhead { left: 96px; top: 90px; width: 412px; height: 583px; }
  .letterhead .address { position: absolute; left: 26px; top: 23px; }
  .letterhead .logo-block { position: absolute; left: 280px; top: 28px; }
  .letterhead .wordmark { font-size: 20px; }
  .letterhead .partner-name { position: absolute; right: 26px; bottom: 30px; font-size: 19px; }

  /* Mouse mat & drink mat */
  .mouse-mat { position: absolute; left: 578px; top: 84px; width: 290px; height: 310px; }
  .drink-mat { position: absolute; left: 927px; top: 177px; width: 176px; height: 176px; border-radius: 50%; overflow: hidden; }
  .scene-photo {
    position: absolute; inset: 0;
    background: linear-gradient(180deg, var(--photo-light) 0%, var(--photo-dark) 100%);
  }
  .mat-logo { position: absolute; }
  .mouse-mat .mat-logo { left: 142px; top: 32px; }
  .mouse-mat .wordmark { font-size: 20px; }
  .mouse-mat .strapline { color: var(--paper); }
  .drink-mat .mat-logo { left: 70px; top: 26px; }
  .drink-mat .wordmark { font-size: 13px; }

  /* Envelope */
  .envelope { left: 578px; top: 437px; width: 474px; height: 199px; }
  .envelope .logo-block { position: absolute; left: 26px; top: 24px; }
  .envelope .wordmark { font-size: 22px; }
  .envelope .address { position: absolute; left: 27px; top: 125px; }

  /* Compliment slip */
  .compliment-slip { left: 578px; top: 682px; width: 359px; height: 179px; }
  .compliment-slip .logo-block { position: absolute; left: 20px; top: 16px; }
  .compliment-slip .wordmark { font-size: 15px; }
  .compliment-slip .strapline { font-size: 4px; margin-top: 4px; }
  .compliment-slip .address { position: absolute; left: 118px; top: 14px; font-size: 4px; }

  /* Business cards */
  .card { position: absolute; top: 734px; width: 174px; height: 99px; }
  .card-back { left: 103px; background: var(--brand-green); }
  .card-back .logo-block { position: absolute; left: 52px; top: 30px; }
  .card-back .wordmark { color: var(--paper); font-size: 18px; }
  .card-back .strapline { color: var(--paper); font-size: 4.5px; }
  .card-front { left: 328px; background: var(--paper); }
  .card-front .logo-block { position: absolute; left: 9px; top: 10px; }
  .card-front .wordmark { font-size: 15px; }
  .card-front .strapline { font-size: 4.5px; margin-top: 5px; }
  .card-front .address { position: absolute; left: 89px; top: 38px; font-size: 6px; }
  .card-front .partner-name { position: absolute; left: 9px; top: 78px; font-size: 10px; }
  .card-front .base-band { position: absolute; left: 0; right: 0; bottom: 0; height: 4px; background: var(--brand-green); }
</style>
</head>
<body>

  <div class="item-label" style="left:261px;top:64px;">Letterhead</div>
  <section class="sheet letterhead">
    <div class="address">
      <div class="company">FERNHOL RAIL</div>
      <div>Harrow Court</div>
      <div>Linden Place</div>
      <div>London SW1A 4QT</div>
      <div>United Kingdom</div>
      <div>+44 (0)20 7946 0321</div>
      <div>www.fernholtrail.co.uk</div>
    </div>
    <div class="logo-block">
      <div class="wordmark">Fernhol Rail</div>
      <div class="strapline">Track Crews<br>True Knowhow</div>
    </div>
    <div class="partner-name">TEMLO</div>
  </section>

  <div class="item-label" style="left:679px;top:52px;">Mouse mats</div>
  <section class="mouse-mat">
    <div class="scene-photo" role="img" aria-label="Photograph of a passenger train crossing a tall stone viaduct under a cloudy sky"></div>
    <div class="mat-logo">
      <div class="wordmark">Fernhol Rail</div>
      <div class="strapline">Track Crews<br>True Knowhow</div>
    </div>
  </section>

  <div class="item-label" style="left:975px;top:142px;">Drink mats</div>
  <section class="drink-mat">
    <div class="scene-photo" role="img" aria-label="Photograph of a passenger train crossing a stone viaduct"></div>
    <div class="mat-logo">
      <div class="wordmark">Fernhol Rail</div>
    </div>
  </section>

  <section class="sheet envelope">
    <div class="logo-block">
      <div class="wordmark">Fernhol Rail</div>
      <div class="strapline">Track Crews<br>True Knowhow</div>
    </div>
    <div class="address">
      <div class="company">FERNHOL RAIL</div>
      <div>Harrow Court</div>
      <div>Linden Place</div>
      <div>London SW1A 4QT</div>
      <div>United Kingdom</div>
      <div>+44 (0)20 7946 0321</div>
      <div>www.fernholtrail.co.uk</div>
    </div>
  </section>
  <div class="item-label" style="left:1073px;top:527px;">Envelopes</div>

  <section class="sheet compliment-slip">
    <div class="logo-block">
      <div class="wordmark">Fernhol Rail</div>
      <div class="strapline">Track Crews<br>True Knowhow</div>
    </div>
    <div class="address">
      <div class="company">FERNHOL RAIL</div>
      <div>Harrow Court</div>
      <div>Linden Place</div>
      <div>London SW1A 4QT</div>
      <div>United Kingdom</div>
      <div>+44 (0)20 7946 0321</div>
      <div>www.fernholtrail.co.uk</div>
    </div>
  </section>
  <div class="item-label" style="left:694px;top:885px;">compliment slips</div>

  <section class="card card-back">
    <div class="logo-block">
      <div class="wordmark">Fernhol Rail</div>
      <div class="strapline">Track Crews<br>True Knowhow</div>
    </div>
  </section>
  <div class="item-label" style="left:129px;top:860px;font-size:12px;">business card (Back)</div>

  <section class="card card-front">
    <div class="logo-block">
      <div class="wordmark">Fernhol Rail</div>
      <div class="strapline">Track Crews<br>True Knowhow</div>
    </div>
    <div class="address">
      <div class="company">FERNHOL RAIL</div>
      <div>Harrow Court</div>
      <div>Linden Place</div>
      <div>London SW1A 4QT</div>
      <div>United Kingdom</div>
      <div>+44 (0)20 7946 0321</div>
      <div>www.fernholtrail.co.uk</div>
    </div>
    <div class="partner-name">TEMLO</div>
    <div class="base-band"></div>
  </section>
  <div class="item-label" style="left:352px;top:860px;font-size:12px;">business card (Front)</div>

</body>
</html>
```